Business card design for a real estate company

We need a business card design a real estate development company called "Quindaro Holding SA" in Switzerland. Space needed for two phone numbers in international format (one is +7 (912) xxx-xx-xx, the other +41 (76) xxx-xx-xx), e-mail (ml@quindaro-example.com), name, position and address of the company:
Rue des Tilleuls 24
CH-1700 Fribourg
Switzerland

Target Market(s)

Potential partners, architects, banks etc..

Industry/Entity Type

Business

Requirements
Must have
• Slight, elegant.
Should not have
• Do not include illustrations of buildings etc..

```html
<!DOCTYPE html>
<html lang="en">
<head>
<meta charset="utf-8">
<title>Quindaro Holding SA – Business Card</title>
<link rel="stylesheet" href="https://fonts.googleapis.com/css2?family=Cinzel:wght@400;600&display=swap">
<style>
  :root {
    --page-bg: #ffffff;
    --card-white: #ffffff;
    --card-edge: #7a7a7a;
    --brand-blue: #0078a6;
    --rule-blue: #1a9ad6;
    --back-blue: #0079a6;
    --back-mark: #0a8ccc;
    --ink-grey: #5a5a5a;
  }
  * { margin: 0; padding: 0; box-sizing: border-box; }
  html, body {
    width: 1200px;
    height: 848px;
    overflow: hidden;
    background: var(--page-bg);
  }
  body {
    position: relative;
    font-family: "Cinzel", serif;
    color: var(--ink-grey);
  }
  .card {
    position: absolute;
    left: 432px;
    width: 357px;
    height: 218px;
  }
  .card--front {
    top: 178px;
    background: var(--card-white);
    border: 1px solid var(--card-edge);
  }
  .card--back {
    top: 437px;
    background: var(--back-blue);
  }
  .line {
    position: absolute;
    left: 0;
    right: 0;
    text-align: center;
    white-space: nowrap;
    line-height: 1;
  }
  .brand-mark {
    top: 26px;
    font-size: 17px;
    font-weight: 400;
    letter-spacing: 2px;
    color: var(--brand-blue);
  }
  .company-name {
    top: 62px;
    font-size: 13.5px;
    letter-spacing: 0.6px;
    color: var(--ink-grey);
  }
  .company-suffix {
    top: 78px;
    font-size: 9px;
    color: var(--ink-grey);
  }
  .rule {
    position: absolute;
    top: 81px;
    height: 1px;
    background: var(--rule-blue);
  }
  .rule--left { left: 91px; width: 77px; }
  .rule--right { left: 191px; width: 75px; }
  .person-name {
    top: 107px;
    font-size: 12px;
    font-weight: 600;
    letter-spacing: 0.5px;
  }
  .person-role {
    top: 122px;
    font-size: 9.5px;
  }
  .contact {
    font-size: 10.5px;
    letter-spacing: 0.1px;
  }
  .contact--address { top: 154px; }
  .contact--phone { top: 172px; }
  .contact--email { top: 190px; font-size: 10px; }
  .back-mark {
    top: 102px;
    font-size: 17px;
    letter-spacing: 2px;
    color: var(--back-mark);
  }
</style>
</head>
<body>
  <section class="card card--front" aria-label="Business card front">
    <div class="line brand-mark">Quindaro</div>
    <div class="line company-name">Quindaro Holding</div>
    <span class="rule rule--left"></span>
    <div class="line company-suffix">SA</div>
    <span class="rule rule--right"></span>
    <div class="line person-name">Elias Berger</div>
    <div class="line person-role">Director</div>
    <div class="line contact contact--address">Rue des Tilleuls 24&nbsp; CH-1700 Fribourg Switzerland</div>
    <div class="line contact contact--phone">Ph: +7 (912) xxx-xx-xx Ph: +41 (76) xxx-xx-xx</div>
    <div class="line contact contact--email">e-mail: ml@quindaro-example.com</div>
  </section>

  <section class="card card--back" aria-label="Business card back">
    <div class="line back-mark">Quindaro</div>
  </section>
</body>
</html>
```